Postcard Design Project

We sells Laser Printer Ink and Toners, We also sells on Zephra Market Place, Need a post card for these zephra contact to start buying through our website instead of Zephra. Company Name: Kv Business Supplies LLC, website is www.kvtoner.example phone#555-203-4471

```html
<!DOCTYPE html>
<html lang="en">
<head>
<meta charset="utf-8">
<title>Kv Business Supplies Postcard</title>
<link href="https://fonts.googleapis.com/css2?family=Roboto+Condensed:wght@700&family=Open+Sans:wght@400;600;700&display=swap" rel="stylesheet">
<style>
  :root {
    --blue-deep: #1b6aa8;
    --blue-bright: #2aa9e1;
    --yellow-deep: #f0c419;
    --yellow-light: #f8ea55;
    --magenta: #e5168a;
    --gray-band: #e2e2e2;
    --charcoal: #333333;
    --ink: #222222;
    --red: #d5252b;
    --white: #ffffff;
    --icon-blue: #2a8fd0;
  }
  html, body {
    margin: 0;
    padding: 0;
    width: 1200px;
    height: 903px;
    overflow: hidden;
    background: #ffffff;
  }
  .postcard {
    position: relative;
    width: 1200px;
    height: 903px;
    overflow: hidden;
    font-family: "Open Sans", Arial, sans-serif;
  }
  .postcard-shapes {
    position: absolute;
    inset: 0;
  }
  .headline {
    position: absolute;
    left: 40px;
    top: 48px;
    margin: 0;
    font-family: "Roboto Condensed", "Arial Narrow", sans-serif;
    font-weight: 700;
    font-size: 76px;
    color: var(--white);
    letter-spacing: 1px;
    line-height: 1;
  }
  .offer {
    position: absolute;
    left: 40px;
    top: 210px;
    margin: 0;
    font-family: "Roboto Condensed", "Arial Narrow", sans-serif;
    font-weight: 700;
    color: var(--ink);
    line-height: 1.05;
  }
  .offer-main { display: block; font-size: 72px; }
  .offer-sub { display: block; font-size: 52px; }
  .ink-note {
    position: absolute;
    left: 40px;
    top: 408px;
    margin: 0;
    font-size: 29px;
    font-weight: 600;
    color: var(--white);
    line-height: 1.3;
  }
  .call-label {
    position: absolute;
    left: 180px;
    top: 512px;
    margin: 0;
    font-size: 29px;
    font-weight: 600;
    color: var(--ink);
  }
  .phone {
    position: absolute;
    left: 42px;
    top: 552px;
    display: flex;
    align-items: center;
    gap: 22px;
  }
  .phone-number {
    font-family: "Roboto Condensed", "Arial Narrow", sans-serif;
    font-weight: 700;
    font-size: 66px;
    color: var(--red);
    line-height: 1;
  }
  .brand {
    position: absolute;
    left: 330px;
    top: 660px;
    display: flex;
    align-items: center;
    gap: 14px;
  }
  .brand-mark {
    width: 42px;
    height: 42px;
    border-radius: 50%;
    background: var(--magenta);
  }
  .brand-name {
    font-size: 32px;
    font-weight: 700;
    color: var(--ink);
  }
  .visit-label {
    position: absolute;
    left: 62px;
    top: 724px;
    margin: 0;
    font-size: 28px;
    font-weight: 600;
    color: var(--ink);
  }
  .website {
    position: absolute;
    left: 150px;
    top: 808px;
    margin: 0;
    font-size: 36px;
    font-weight: 400;
    letter-spacing: 6px;
    color: var(--white);
  }
</style>
</head>
<body>
<main class="postcard">
  <svg class="postcard-shapes" width="1200" height="903" viewBox="0 0 1200 903" xmlns="http://www.w3.org/2000/svg">
    <defs>
      <linearGradient id="band-blue" x1="0" y1="0" x2="1" y2="0">
        <stop offset="0" stop-color="var(--blue-deep)"/>
        <stop offset="1" stop-color="var(--blue-bright)"/>
      </linearGradient>
      <linearGradient id="band-yellow" x1="0" y1="0" x2="1" y2="0">
        <stop offset="0" stop-color="var(--yellow-deep)"/>
        <stop offset="1" stop-color="var(--yellow-light)"/>
      </linearGradient>
      <linearGradient id="photo-tones" x1="0" y1="0" x2="1" y2="1">
        <stop offset="0" stop-color="#efe9e2"/>
        <stop offset="0.45" stop-color="#b9b6b4"/>
        <stop offset="0.75" stop-color="#6f6460"/>
        <stop offset="1" stop-color="#3e3a3c"/>
      </linearGradient>
    </defs>

    <rect class="band-blue" x="0" y="0" width="1200" height="185" fill="url(#band-blue)"/>
    <rect class="band-yellow" x="0" y="185" width="1200" height="205" fill="url(#band-yellow)"/>
    <rect class="band-magenta" x="0" y="390" width="1200" height="115" fill="var(--magenta)"/>
    <rect class="band-gray" x="0" y="505" width="1200" height="130" fill="var(--gray-band)"/>
    <rect class="band-white" x="0" y="635" width="1200" height="268" fill="var(--white)"/>
    <path class="visit-tab" d="M0 712 H300 Q330 712 340 740 L352 790 H0 Z" fill="var(--yellow-deep)"/>
    <path class="footer-band" d="M0 775 H700 Q760 775 800 810 L900 903 H0 Z" fill="var(--charcoal)"/>
    <path class="corner-accent" d="M1200 560 V903 H880 Z" fill="var(--magenta)"/>

    <polygon class="photo-frame" points="880,22 1290,440 900,858 505,440" fill="var(--white)" stroke="var(--white)" stroke-width="34" stroke-linejoin="round"/>
    <polygon class="photo-area" role="img" aria-label="Photo of a smiling technician giving a thumbs up beside an opened colour laser printer with toner cartridges" points="880,22 1290,440 900,858 505,440" fill="url(#photo-tones)" stroke="#111111" stroke-width="6" stroke-linejoin="round"/>
  </svg>

  <h1 class="headline">GOT DIRTY PRINTER?</h1>
  <h2 class="offer">
    <span class="offer-main">GET A TECHNICIAN</span>
    <span class="offer-sub">IN YOUR OFFICE TODAY</span>
  </h2>
  <p class="ink-note">Also check out our unbeatable<br>Ink and toner online prices.</p>

  <p class="call-label">Call Us Today</p>
  <div class="phone">
    <svg class="phone-icon" width="48" height="48" viewBox="0 0 48 48" xmlns="http://www.w3.org/2000/svg" aria-hidden="true">
      <circle cx="24" cy="24" r="21" fill="none" stroke="var(--icon-blue)" stroke-width="2.5"/>
      <path d="M16 13 l5 -1 l3 7 l-3 2 q2 5 7 8 l2 -3 l7 3 l-1 5 q-3 3 -8 1 q-10 -5 -14 -15 q-1 -5 2 -7 z" fill="var(--icon-blue)"/>
    </svg>
    <span class="phone-number">555-203-4471</span>
  </div>

  <div class="brand">
    <span class="brand-mark"></span>
    <span class="brand-name">Kv Business Supplies</span>
  </div>

  <p class="visit-label">Visit Us online:</p>
  <p class="website">www.kvtoner.example</p>
</main>
</body>
</html>
```